Yard sign

I want it to look similar to this one,

change name to DRAVEK and submit new ideas

Also would like to improvise a bit. let's not make exactly the same thing

would like to change to: Connecticut #1 Company

also change phone to 203-555-0147
and website to
dravekllc.com

this is yard sign. size is 24' Width and 32' Height

Target Market(s)

Roof

Industry/Entity Type

Roofing

Requirements
Must have
• similar colors or add something new

```html
<!DOCTYPE html>
<html lang="en">
<head>
<meta charset="utf-8">
<title>Dravek Yard Sign Concepts</title>
<link href="https://fonts.googleapis.com/css2?family=Rubik:wght@800;900&family=Saira:wght@600&display=swap" rel="stylesheet">
<style>
  :root{
    --lime:#8cc540;
    --ink:#231f20;
    --black:#0a0a0a;
    --red:#c1202f;
    --red-deep:#8a1620;
    --yellow:#f7ec22;
    --sky:#27a9e1;
    --navy:#2b2a5e;
    --white:#ffffff;
  }
  html,body{margin:0;padding:0;width:1200px;height:900px;overflow:hidden;background:var(--white);}
  .canvas{position:relative;width:1200px;height:900px;}
  .sign{position:absolute;top:102px;width:492px;height:695px;overflow:hidden;}
  .sign--green{left:82px;}
  .sign--yellow{left:646px;}
  .sign svg{display:block;width:492px;height:695px;overflow:hidden;}
  .t-head{font-family:'Rubik',sans-serif;font-weight:900;}
  .t-name{font-family:'Rubik',sans-serif;font-weight:800;letter-spacing:2px;}
  .t-web{font-family:'Saira',sans-serif;font-weight:600;letter-spacing:3px;}
</style>
</head>
<body>
<div class="canvas">

  <!-- Green concept -->
  <div class="sign sign--green">
    <svg viewBox="0 0 492 695" aria-label="Connecticut number one roof company yard sign, green version">
      <rect class="panel-base" width="492" height="695" fill="var(--ink)"/>
      <polygon class="panel-top" points="0,0 492,0 492,316 0,413" fill="var(--lime)"/>

      <g class="headline" transform="rotate(-11 250 250)">
        <text class="t-head" x="40" y="150" font-size="44" fill="var(--ink)">CONNECTICUT #1</text>
        <polygon class="arrow-depth" points="48,232 390,232 390,190 474,292 390,392 390,350 48,350" fill="var(--red-deep)"/>
        <polygon class="arrow" points="40,222 382,222 382,180 466,282 382,382 382,340 40,340" fill="var(--red)" stroke="var(--yellow)" stroke-width="4" stroke-linejoin="round"/>
        <text class="t-head roof-depth" x="58" y="282" font-size="128" fill="var(--red-deep)">ROOF</text>
        <text class="t-head roof" x="50" y="274" font-size="128" fill="var(--red)" stroke="var(--yellow)" stroke-width="4" paint-order="stroke">ROOF</text>
        <text class="t-head" x="62" y="328" font-size="50" fill="var(--yellow)">COMPANY</text>
      </g>

      <text class="t-name" x="206" y="505" font-size="76" fill="var(--lime)" text-anchor="middle">DRAVEK</text>
      <circle class="name-dot" cx="396" cy="452" r="13" fill="var(--lime)"/>

      <rect class="phone-band" y="540" width="492" height="66" fill="var(--sky)"/>
      <g class="phone-icon" transform="translate(22 556)" fill="var(--white)">
        <path d="M6 2c2-2 4-1 5 1l3 5c1 2 0 3-1 4l-2 2c1 3 4 6 7 7l2-2c1-1 2-2 4-1l5 3c2 1 3 3 1 5l-3 3c-3 2-9 0-15-6S2 8 4 5z"/>
      </g>
      <text class="t-head" x="83" y="592" font-size="50" fill="var(--navy)">203-555-0147</text>
      <text class="t-head" x="80" y="589" font-size="50" fill="var(--white)">203-555-0147</text>

      <text class="t-web" x="246" y="660" font-size="30" fill="var(--lime)" text-anchor="middle">www.DravekLLC.com</text>
    </svg>
  </div>

  <!-- Yellow concept -->
  <div class="sign sign--yellow">
    <svg viewBox="0 0 492 695" aria-label="Connecticut number one roof company yard sign, yellow version">
      <rect class="panel-base" width="492" height="695" fill="var(--ink)"/>
      <polygon class="panel-top" points="0,0 492,0 492,285 0,390" fill="var(--yellow)"/>

      <polygon class="badge-box" points="367,20 464,2 464,78 367,100" fill="var(--ink)"/>
      <text class="t-head badge-text" transform="translate(382 82) rotate(-14)" font-size="50" fill="var(--yellow)">#1</text>

      <text class="t-head" transform="translate(34 163) rotate(-14)" font-size="40" fill="var(--black)">CONNECTICUT</text>

      <g class="roof-word" transform="translate(40 308) rotate(-14)">
        <text class="t-head roof-shadow" x="6" y="6" font-size="140" fill="var(--white)">ROOF</text>
        <text class="t-head roof" x="0" y="0" font-size="140" fill="var(--black)">ROOF</text>
      </g>

      <g class="arrow-band" transform="translate(0 400) rotate(-14)">
        <polygon class="arrow" points="-30,-40 400,-40 400,-80 480,-5 400,70 400,30 -30,30" fill="var(--red)"/>
        <text class="t-head" x="40" y="20" font-size="58" fill="var(--yellow)">COMPANY</text>
      </g>

      <text class="t-name" x="244" y="523" font-size="76" fill="var(--yellow)" text-anchor="middle">DRAVEK</text>
      <circle class="name-dot" cx="428" cy="470" r="13" fill="var(--yellow)"/>

      <rect class="phone-band" y="553" width="492" height="67" fill="var(--yellow)"/>
      <g class="phone-icon" transform="translate(32 570)" fill="var(--black)">
        <path d="M6 2c2-2 4-1 5 1l3 5c1 2 0 3-1 4l-2 2c1 3 4 6 7 7l2-2c1-1 2-2 4-1l5 3c2 1 3 3 1 5l-3 3c-3 2-9 0-15-6S2 8 4 5z"/>
      </g>
      <text class="t-head" x="86" y="604" font-size="47" fill="var(--black)">203-555-0147</text>

      <text class="t-web" x="246" y="662" font-size="32" fill="var(--red)" text-anchor="middle">www.DravekLLC.com</text>
    </svg>
  </div>

</div>
</body>
</html>
```